Design a Brochure & Business Cards for a Medical Billing Company

We need business cards, and a trifold brochure, for QUILL Medical Billing, Inc., the “QUILL” represents “quality unified insurance - lasting leverage”. They are a medical billing and revenue management team, providing services to private medical practices.

We have attached the company logo, and copy for the brochure. We have also attached some stock photography that we have purchased for use in the brochure, so feel free to use them in your design, for this project ONLY.

We have also attached an old brochure design, which the client was very happy with, but it is NOT TO BE COPIED in any way. They do not want the media for the new company, to look anything like the old. This is simply attached so you can see what has made the client happy in the past.

The brochure should be a trifold design. Please see the old brochure design for layout (attached), and locations of pertinent info.

Business cards should include the company logo, name, title, phone number, website, and email. The website will be quillmedclaim.example. Configuration and design, we will leave to you. Just as long as it compliments the brochure.

The business cards and brochure MUST complement each other! These items will be presented together to prospective clients, so they must look the part.

We are looking for modern design/s that emphasizes the brand we have created for the client (logo attached). Artwork must be clean, and professional. This is a professional company, dealing with health care providers, so they must look the part. Also, cost of printing should be kept in mind when considering your use of colors.

All final designs must be ready for print. This means 300 dpi, with proper margins and bleed.

```html
<!DOCTYPE html>
<html lang="en">
<head>
<meta charset="utf-8">
<title>QUILL Medical Billing – Trifold Brochure</title>
<link rel="stylesheet" href="https://fonts.googleapis.com/css2?family=Arimo:wght@400;700&display=swap">
<style>
:root{
  --backdrop:#e6e6e6;
  --paper:#ffffff;
  --navy:#1f4d8f;
  --teal:#1b9bb1;
  --ink:#3a3a3a;
}
*{box-sizing:border-box;margin:0;padding:0}
html,body{width:1200px;height:891px;overflow:hidden;background:var(--backdrop)}
body{font-family:"Arimo",Arial,sans-serif;color:var(--ink);position:relative}
.brochure{position:absolute;left:100px;top:91px;width:1000px;height:707px;background:var(--paper);box-shadow:0 4px 12px rgba(0,0,0,.25);overflow:hidden}
.photo{position:absolute;top:0;height:229px}
.photo--claim{left:0;width:667px;background:linear-gradient(160deg,#f3f1ee 0%,#dcdcdc 45%,#c9ccd0 100%)}
.photo--statement{left:667px;width:333px;background:linear-gradient(200deg,#e9ecef 0%,#c4cbd2 55%,#9aa4ad 100%)}
.header-rule{position:absolute;top:229px;left:0;width:1000px;height:4px;background:var(--teal)}
.panel{position:absolute;top:233px;width:333.4px;height:474px;display:flex;flex-direction:column}
.panel--left{left:0}
.panel--middle{left:333.3px}
.panel--right{left:666.6px}
.panel-title{flex:none;height:22px;font-size:9.5px;font-weight:700;letter-spacing:.2px;color:#fff;text-transform:uppercase;display:flex;align-items:center;white-space:nowrap}
.panel-title--left{background:var(--navy);width:228px;padding-left:30px}
.panel-title--middle{background:var(--teal);width:242px;margin:0 auto;justify-content:center}
.panel-title--right{background:var(--navy);width:228px;margin-left:auto;justify-content:flex-end;padding-right:30px}
.copy{flex:1;padding:18px 30px 0;font-size:9.3px;line-height:1.24;text-align:justify}
.copy p{margin-bottom:10px}
.tab{background:var(--teal);color:#fff;font-size:10.5px;font-weight:700;text-align:center;padding:4px 0;margin:2px 0 8px}
.feature{flex:none;color:#fff;font-size:9.3px;line-height:1.24;padding:12px 30px;text-align:justify}
.feature p+p{margin-top:10px}
.feature--left{height:141px;background:var(--teal)}
.feature--middle{height:88px;background:var(--navy)}
.feature--right{height:62px;background:var(--teal);font-size:7.4px;line-height:1.3;padding-top:10px;text-align:left}
.arrow-list,.check-list{list-style:none;text-align:left}
.arrow-list li{position:relative;padding-left:18px;margin-bottom:5px}
.arrow-list li::before{content:"";position:absolute;left:2px;top:2px;width:10px;height:8px;background:var(--teal);clip-path:polygon(0 30%,55% 30%,55% 0,100% 50%,55% 100%,55% 70%,0 70%)}
.check-list li{position:relative;padding-left:18px;margin-bottom:3px}
.check-list li::before{content:"";position:absolute;left:2px;top:2px;width:8px;height:8px;border-radius:50%;background:var(--teal)}
.arrow-list--tight li{margin-bottom:3px}
</style>
</head>
<body>
<main class="brochure">
  <div class="photo photo--claim" role="img" aria-label="Photo of an insurance claim form with a binder clip"></div>
  <div class="photo photo--statement" role="img" aria-label="Photo of a billing statement with a stethoscope"></div>
  <div class="header-rule"></div>

  <section class="panel panel--left">
    <h2 class="panel-title panel-title--left">Regain control of your business</h2>
    <div class="copy">
      <p>The economy is questionable and in some turmoil, the Affordable Care Act is impacting your patient’s choices and coverage not to mention putting more pressure on your office requirements for EMR management, your current billing service is cherry picking only your largest charges and the easy parts of your revenue cycle.</p>
      <p>Does any of this sound familiar to you?<br>Do you feel like your practice is nearing a Code Blue?</p>
      <p>QUILL Medical Billing is here to help you stop the bleeding and regain control of your business while allowing you to be what you been trained and have a passion for – being a healer.</p>
      <div class="tab">SIZE DOESN’T MATTER</div>
      <p>Regardless of your practice size, or your location, QUILL Medical Billing, Inc. (QUILL) can assist you in restoring your practice to good health.</p>
    </div>
    <div class="feature feature--left">
      <p>The owners of QUILL have nearly thirty years of experience in medical office and billing services and another 30 years in building and managing electronic systems, managing consultants, professional software sales, and support.</p>
      <p>We can help you optimize your revenue cycle without you needing to hire additional employees, which would increase your benefit and personnel management costs; instead you can focus on what you do best – patient care.</p>
    </div>
  </section>

  <section class="panel panel--middle">
    <h2 class="panel-title panel-title--middle">Start off on the right path immediately</h2>
    <div class="copy">
      <p>At QUILL we see many practices struggling in the medical environment. We launched QUILL with a vision to assist practices in maximizing their reimbursement by providing an exceptional level of service to assist with managing the revenue cycle so that providers can spend more time serving patients rather than chasing money.</p>
      <p>No service can guarantee there will never be an error, but QUILL staff will continuously review procedures, counsel staff, and invest in training to be sure that we stay “at the top of our game”. If you are a new practice/provider, why not start off on the right path immediately and let QUILL help you maximize your reimbursement from both insurance payers and patients from the beginning?</p>
      <div class="tab">Our goal is zero defects in the revenue cycle</div>
      <ul class="arrow-list">
        <li>We have experience with the major clearinghouses and medical electronic filing/billing tools.</li>
        <li>We keep abreast of all the latest changes and mandates in the healthcare industry (e.g., ICD-10 requirements).</li>
        <li>We have experience with many of the different practice management software systems and our fees are comparable if not lower than most billing services.</li>
        <li>We will evaluate your practice size, claim volume, payer mix, and total dollars owed to you greater than 90 days to determine the best rate for your practice.</li>
      </ul>
    </div>
    <div class="feature feature--middle">
      <p>The monthly fee we charge is tied to our own performance because it is based on how successful we are in retrieving your revenue – we only get paid if you do, and since we bill you based on a percentage of collected revenue the only way for us to increase our revenue is to increase yours!</p>
    </div>
  </section>

  <section class="panel panel--right">
    <h2 class="panel-title panel-title--right">We only get paid if you do</h2>
    <div class="copy">
      <p>Our business drive is to maximize your revenue and shorten the claim adjudication process by submitting clean claims.</p>
      <div class="tab">OUR SERVICES</div>
      <p>Listed below are the ways in which we will assist your practice in attaining a “healthy report card” for your accounts receivable.</p>
      <ul class="arrow-list arrow-list--tight">
        <li>Reduce billing days and claim rejection rates</li>
        <li>Lower the file-to-collection cycle</li>
        <li>Ensure receipt of proper reimbursement from payers</li>
        <li>Obtain higher average returns per processed claim</li>
        <li>Reduce aged AR accounts and the cost to collect and minimize denial write-offs</li>
      </ul>
      <div class="tab">REASONS TO OUTSOURCE YOUR BILLING</div>
      <ul class="check-list">
        <li>Revenue increases</li>
        <li>Cleaner claim submissions</li>
        <li>Improved results</li>
        <li>Response to changing regulations is improved</li>
        <li>Internal personnel costs are reduced</li>
        <li>Focus on patient care instead of accounting and/or personnel management</li>
        <li>(*) Improve patient satisfaction – a more clear and concise patient billing experience</li>
        <li>Obtain a billing staff that is experienced and committed to your success</li>
      </ul>
    </div>
    <div class="feature feature--right">
      <p>(*)When your patients call us with questions about their statements they will be treated with the utmost respect and courtesy while attempting to provide them with all the information they need to answer their questions fully.</p>
    </div>
  </section>
</main>
</body>
</html>
```